Need to make a KMB water label for my water bottle and packaging. Attached is our Trademarked LOGO for KMB we have a natural spring water that flows through our land that is naturally filtered through pure limestone. want to make a badass label that has our logo in it with our colors

Target Market(s)

Commercial Bottle water

Colors
3176b5

```html
<!DOCTYPE html>
<html lang="en">
<head>
<meta charset="utf-8">
<title>KMB Spring Water Label</title>
<link rel="stylesheet" href="https://fonts.googleapis.com/css2?family=Arimo:ital,wght@0,400;0,700;1,700&display=swap">
<style>
  :root {
    --brand-blue: #3176b5;
    --deep-blue: #1f5f9e;
    --sky-blue: #8fc3ea;
    --mist: #e9f4fb;
    --navy: #14233f;
    --silver-light: #eef0f2;
    --silver-dark: #a9adb2;
    --white: #ffffff;
    --ink: #2b2f36;
  }
  * { box-sizing: border-box; margin: 0; padding: 0; }
  html, body { width: 1200px; height: 325px; overflow: hidden; background: var(--white); }
  .label {
    position: relative;
    width: 1200px;
    height: 325px;
    overflow: hidden;
    font-family: "Arimo", Arial, sans-serif;
    background:
      linear-gradient(180deg, var(--brand-blue) 0%, var(--sky-blue) 30%, var(--mist) 62%, var(--sky-blue) 86%);
  }
  .product-story {
    position: absolute;
    left: 28px;
    top: 30px;
    width: 290px;
    color: var(--white);
  }
  .product-story h2 {
    font-size: 17px;
    font-weight: 700;
    margin-bottom: 3px;
  }
  .product-story p {
    font-size: 16.5px;
    line-height: 20px;
  }
  .water-splash {
    position: absolute;
    left: 330px;
    top: 0;
    width: 600px;
    height: 276px;
  }
  .brand-name {
    position: absolute;
    left: 430px;
    top: 92px;
    width: 200px;
    text-align: center;
    font-size: 86px;
    font-weight: 700;
    letter-spacing: 2px;
    color: var(--deep-blue);
  }
  .volume {
    position: absolute;
    left: 790px;
    top: 178px;
    font-size: 16px;
    line-height: 20px;
    color: var(--ink);
    text-align: center;
  }
  .tagline-band {
    position: absolute;
    left: 0;
    top: 276px;
    width: 1200px;
    height: 49px;
    background: linear-gradient(180deg, var(--silver-light) 0%, var(--silver-dark) 100%);
    border-top: 2px solid var(--white);
    display: flex;
    align-items: center;
    justify-content: center;
    padding-right: 0;
  }
  .tagline-band p {
    font-size: 19px;
    font-weight: 700;
    font-style: italic;
    color: var(--navy);
    letter-spacing: 0.2px;
  }
  .upc-panel {
    position: absolute;
    left: 930px;
    top: 16px;
    width: 110px;
    height: 254px;
    background: var(--white);
    display: flex;
    align-items: center;
    justify-content: center;
  }
  .vertical-text {
    writing-mode: vertical-rl;
    transform: rotate(180deg);
    color: var(--navy);
    font-size: 18px;
    line-height: 22px;
    text-align: center;
  }
  .distributor {
    position: absolute;
    left: 1058px;
    top: 16px;
    height: 254px;
    display: flex;
    align-items: center;
  }
  .quality-contact {
    position: absolute;
    left: 1118px;
    top: 16px;
    height: 254px;
    display: flex;
    align-items: center;
  }
</style>
</head>
<body>
  <main class="label">
    <section class="product-story">
      <h2>Product Story Here</h2>
      <p>Product story here, product story here, product story here. Product story here, product story here, product story here. Product story here, product story here, product story here, product story here, product story here, product story here.</p>
    </section>

    <svg class="water-splash" viewBox="0 0 600 276" role="img" aria-label="Illustration of a swirling splash of clear spring water with droplets">
      <defs>
        <radialGradient id="splashTone" cx="50%" cy="55%" r="55%">
          <stop offset="0%" stop-color="#ffffff" stop-opacity="0.95"/>
          <stop offset="45%" stop-color="#cfe7f7" stop-opacity="0.85"/>
          <stop offset="80%" stop-color="#5c9fd6" stop-opacity="0.55"/>
          <stop offset="100%" stop-color="#3176b5" stop-opacity="0"/>
        </radialGradient>
      </defs>
      <ellipse cx="230" cy="150" rx="230" ry="125" fill="url(#splashTone)"/>
    </svg>

    <div class="brand-name">KMB</div>

    <div class="volume">16.9 FL OZ.<br>(1.05 PT) 500ml</div>

    <div class="upc-panel">
      <p class="vertical-text">UPC CODE HERE</p>
    </div>

    <div class="distributor">
      <p class="vertical-text">DISTRIBUTED BY ABCDEFGHU<br>SOMEWHERE USA</p>
    </div>

    <div class="quality-contact">
      <p class="vertical-text">FOR WATER QUALITY<br>CONTACT 555-010-0199</p>
    </div>

    <footer class="tagline-band">
      <p>NATURAL SPRING WATER-NATURALLY FILTERED THROUGH PURE LIMESTONE</p>
    </footer>
  </main>
</body>
</html>
```